Product Description page for Hullwrap.com, References here just need a clean up redesign

Hi, were working on updating the product description page of our site hullwrap.com

Attached is a reference of what we drew on paint. We want to keep it pretty much the same as far as whats on there, the components with a few small adjustments and a clean actually designed look.

1. We want to remove the tabs (product description, warranty, reviews) and put it all in that main content area stretching down into sections. IE: Product Description section, followed by reviews, followed by warranty, below each other.
2. The side bar needs to be redesigned as far as the look and feel but the content and whats in there should stay the same.
3. The main banner area will be replaced shortly you do not have to worry about that.
4. Include a section or box for people to put in their email for a free Ebook.

Target Market(s)

people looking to easily view our boat cover products and buy without having to click too often or leave the page.

Industry/Entity Type

Online Shopping

Number of Pages Required

1 page

Requirements
Must have
• - Must update the sidebar
• - Must update the content area to remove the tabs and put the content from each tab sectioned off below each other (dummy text is fine for now for the tabs you cant view)
Nice to have
• - Cool place thats clean and functional to insert a section for people to put in their email to receive a free ebook
Should not have
• - too much change, we already know what we want and have a solid reference to work from.

```html
<!DOCTYPE html>
<html lang="en">
<head>
<meta charset="utf-8">
<title>Hullwrap.com – Centre Console With Bow Rails</title>
<link href="https://fonts.googleapis.com/css2?family=Lato:wght@400;700;900&display=swap" rel="stylesheet">
<style>
:root{
  --ink:#3a3a3a;
  --ink-soft:#555;
  --blue:#2a8cc0;
  --navy:#1a3aa8;
  --red:#d40000;
  --orange:#ff7a00;
  --green:#2c9a3c;
  --bar:#4b4e51;
  --panel:#e8e8e8;
  --line:#cfcfcf;
  --nav-top:#fbfbfb;
  --nav-bot:#e1e1e1;
}
*{box-sizing:border-box;margin:0;padding:0}
html,body{width:1200px;height:1135px;overflow:hidden;background:#fff}
body{font-family:'Lato',sans-serif;color:var(--ink);position:relative}

.header{position:absolute;left:0;top:0;width:1200px;height:56px;background:#fff}
.brand{position:absolute;left:218px;top:13px;display:flex;align-items:center;gap:9px}
.brand-mark{width:22px;height:22px;background:var(--blue)}
.brand-name{font-size:25px;font-weight:900;color:var(--ink);line-height:28px}
.contact{position:absolute;right:216px;top:9px;text-align:right}
.phone{font-size:20px;color:var(--blue);display:flex;align-items:center;gap:3px;justify-content:flex-end}
.hours{font-size:10px;color:var(--ink-soft)}

.nav{position:absolute;left:0;top:56px;width:1200px;height:34px;background:linear-gradient(var(--nav-top),var(--nav-bot));border-top:1px solid #eee}
.nav ul{list-style:none;position:absolute;left:202px;top:0;display:flex;height:34px}
.nav li{font-size:12.5px;color:var(--ink-soft);padding:0 15px;line-height:34px;border-right:1px solid #cfcfcf}
.checkout{position:absolute;left:830px;top:0;width:152px;height:34px;background:var(--blue);color:#fff;font-size:11.5px;font-weight:700;display:flex;align-items:center;justify-content:center;gap:5px}
.checkout small{font-size:8.5px;font-weight:400}

.crumbs{position:absolute;left:0;top:90px;width:1200px;height:32px;background:var(--bar);color:#fff;font-size:12.5px;line-height:32px;padding-left:219px}
.crumbs b{font-weight:700}

.page{position:absolute;left:216px;top:122px;width:768px;height:1013px;border-left:1px solid var(--line);border-right:1px solid var(--line)}

.hero{position:absolute;left:246px;top:152px;width:482px;height:252px;background:radial-gradient(ellipse at 50% 45%,#c9cbcf 0%,#e6e7ea 45%,#fff 75%)}
.thumbs{position:absolute;left:246px;top:426px;width:482px;height:86px;background:#fff;border:1px solid #e4e4e4}
.thumbs .arrow{position:absolute;top:0;width:24px;height:86px;background:#e6e6e6;display:flex;align-items:center;justify-content:center}
.thumbs .tile{position:absolute;top:14px;width:60px;height:57px;border:1px solid #ccc}

.divider{position:absolute;left:216px;width:546px;height:1px;background:var(--line)}
.section-title{position:absolute;left:230px;font-size:19.5px;font-weight:700;color:var(--blue)}
.desc{position:absolute;left:230px;top:597px;width:500px;font-size:13.6px;line-height:17.3px;color:var(--ink)}
.feat-title{position:absolute;left:229px;top:683px;font-size:13.6px;font-weight:700}
.features{position:absolute;left:243px;top:708px;width:420px;list-style:none;font-size:13.6px;line-height:19.2px}
.features li{position:relative}
.features li::before{content:"";position:absolute;left:-13px;top:8px;width:4px;height:4px;border-radius:50%;background:#bbb}

.review{position:absolute;left:232px;width:502px;font-size:13.6px;line-height:17.3px}
.review q{quotes:"\201C" "\201D"}
.review q::before,.review q::after{color:var(--navy)}
.reviewer{position:absolute;font-size:13.6px;color:var(--navy);display:flex;align-items:center;gap:14px}
.stars{display:flex;gap:1px}
.rule{position:absolute;left:268px;top:1040px;width:427px;height:1px;background:var(--navy)}

.side{position:absolute;left:762px;top:122px;width:221px}
.p-title{position:absolute;left:0;top:18px;font-size:20px;font-weight:900;line-height:20px;color:var(--ink)}
.p-sub{position:absolute;left:0;top:63px;font-size:10.5px;font-weight:700;color:#777}
.was{position:absolute;left:0;top:86px;font-size:14px;text-decoration:line-through;color:var(--ink-soft)}
.save{position:absolute;left:1px;top:104px;font-size:13.5px}
.save b{color:var(--red);font-weight:700}
.price{position:absolute;left:0;top:122px;font-size:27px;font-weight:900;color:var(--red)}
.opt{position:absolute;left:0;font-size:14px;color:var(--ink-soft)}
.select{position:absolute;left:76px;width:122px;height:24px;border:1px solid #999;font-size:10px;color:#555;padding:5px 8px;background:#fff}
.select::after{content:"";position:absolute;right:10px;top:10px;border:4px solid transparent;border-top:5px solid #333}

.box-head{position:absolute;left:0;width:221px;height:42px;background:var(--bar);color:#fff;font-size:14.5px;padding-left:8px;line-height:42px}
.box-body{position:absolute;left:0;width:221px;background:var(--panel)}
.item{position:absolute;left:8px;width:200px}
.item .pic{position:absolute;left:0;top:0;width:75px;height:66px;border:2px solid #555;background:linear-gradient(#f4f4f4,#d5d5d5)}
.item .info{position:absolute;left:85px;top:0;width:125px}
.item h4{font-size:14px;font-weight:700;color:var(--ink-soft);line-height:14px}
.item p{font-size:11.5px;line-height:11.5px;color:var(--ink-soft)}
.item .free{font-size:15px;color:var(--red);line-height:19px;padding-left:2px}
.item .cost{font-size:14px;color:var(--blue);display:flex;align-items:center;gap:5px;line-height:20px}
.chk{width:12px;height:12px;border:1px solid #444;background:#fff;position:relative}
.cart-btn{position:absolute;left:10px;top:636px;width:200px;height:38px;background:linear-gradient(#ff8a10,#ff6a00);color:#fff;font-size:20px;font-weight:900;text-align:center;line-height:38px}
.ship{position:absolute;left:0;width:221px;top:682px;text-align:center;font-size:14px;color:var(--green);display:flex;justify-content:center;align-items:center;gap:6px}
.indoor-pic{position:absolute;left:38px;top:762px;width:144px;height:68px;background:radial-gradient(ellipse at 50% 40%,#2f6db3 0%,#7aa0c8 50%,var(--panel) 80%)}
.indoor-name{position:absolute;left:0;top:839px;width:221px;text-align:center;font-size:14px;font-weight:700;line-height:14px;color:var(--ink-soft)}
.indoor-price{position:absolute;left:0;top:869px;width:221px;text-align:center;font-size:14px}
.indoor-price s{color:var(--ink-soft);margin-right:5px}
.indoor-price span{color:var(--red)}
</style>
</head>
<body>

<header class="header">
  <div class="brand"><span class="brand-mark"></span><span class="brand-name">Hullwrap.com</span></div>
  <div class="contact">
    <div class="phone">
      <svg width="27" height="20" viewBox="0 0 27 20"><path d="M2 7c0-4 6-6 11.5-6S25 3 25 7l-4 1-1-3h-13l-1 3z" fill="#2a8cc0"/><rect x="5" y="9" width="17" height="10" rx="3" fill="#2a8cc0"/><circle cx="13.5" cy="14" r="3" fill="#fff"/></svg>
      (800)555-0142
    </div>
    <div class="hours">Store Hours (M-F,9:30-6PM PST)</div>
  </div>
</header>

<nav class="nav">
  <ul>
    <li>Boat Covers</li><li>Bass</li><li>Boat Covers</li><li>T Top Boat Covers</li><li>Bimini Tops</li><li>Jet Ski Covers</li>
  </ul>
  <div class="checkout">
    <svg width="15" height="13" viewBox="0 0 15 13"><path d="M1 1h2l2 7h7l2-5H4" fill="none" stroke="#fff" stroke-width="1.4"/><circle cx="6" cy="11" r="1.3" fill="#fff"/><circle cx="11" cy="11" r="1.3" fill="#fff"/></svg>
    CHECK OUT : <small>0 items ▾</small>
  </div>
</nav>

<div class="crumbs">Home &gt;&gt; Boat Covers &gt;&gt; Centre Console With Bow Rails &gt;&gt; <b>Up To 16'8" Long And 90" Wide</b></div>

<main class="page"></main>

<div class="hero" role="img" aria-label="Grey boat cover strapped over a centre console boat on a trailer"></div>

<div class="thumbs">
  <div class="arrow" style="left:0"><svg width="10" height="16"><path d="M8 1 2 8l6 7" fill="none" stroke="#fff" stroke-width="3"/></svg></div>
  <div class="tile" role="img" aria-label="Five star fit badge" style="left:48px;background:linear-gradient(#fff,#ddd)"></div>
  <div class="tile" role="img" aria-label="Blue fabric layer detail" style="left:117px;background:linear-gradient(#2a63a8,#4d8ad0)"></div>
  <div class="tile" role="img" aria-label="Cover strap detail" style="left:186px;background:linear-gradient(#bbb,#888)"></div>
  <div class="tile" role="img" aria-label="Buckle strap on cover" style="left:255px;background:linear-gradient(#d8d8d8,#9a9a9a)"></div>
  <div class="tile" role="img" aria-label="Black strap close-up" style="left:324px;background:linear-gradient(#555,#222)"></div>
  <div class="tile" role="img" aria-label="Strap and buckle pack" style="left:393px;background:linear-gradient(#eee,#aaa)"></div>
  <div class="arrow" style="right:0"><svg width="10" height="16"><path d="M2 1l6 7-6 7" fill="none" stroke="#fff" stroke-width="3"/></svg></div>
</div>

<div class="divider" style="top:547px"></div>
<h2 class="section-title" style="top:563px">Product Discription :</h2>
<p class="desc">The Tidewell Supreme is the most powerful cover available providing 10x more strength and protection compared to the competition. The 1200 denier fabric is 100% waterproof and provides excellent protection against sun, rain, wind and snow.</p>
<div class="feat-title">Features:</div>
<ul class="features">
  <li>5 Star Fit. Fit guaranteed or your money back</li>
  <li>10 Year Warranty. Full warranty covering rips and tears</li>
  <li>The fabric is pure 100% Marine Polyester (no cotton mix)</li>
  <li>No worries, the cover won't stretch or shrink</li>
  <li>Rain or sleet the cover is 100% waterproof</li>
  <li>Fully Breathable, you'll never see mold or mildew</li>
  <li>UV resistant and also prevents heat buildup</li>
  <li>The cover also comes with an integrated hem cord to be used when mooring or on boat lifts</li>
  <li>Tough - Strong - Durable</li>
</ul>

<div class="divider" style="top:925px"></div>
<h2 class="section-title" style="top:937px;left:232px">Reviews :</h2>
<p class="review" style="top:971px"><q>This item is quite heavy duty and rides well. It is also great quality. We are pleased with the cover and I would recommend it to anyone who wants a great fit and strong cover.</q></p>
<div class="reviewer" style="left:572px;top:1008px">Marcus T.
  <span class="stars">
    <svg width="72" height="16" viewBox="0 0 72 16"><g fill="#ffd21f" stroke="#c9a000" stroke-width=".6"><path id="st" d="M8 .8l2.2 4.6 5 .6-3.7 3.4 1 5-4.5-2.5-4.5 2.5 1-5L.8 6l5-.6z"/><use href="#st" x="18"/><use href="#st" x="36"/><use href="#st" x="54"/></g></svg>
  </span>
</div>
<div class="rule"></div>
<p class="review" style="top:1052px"><q>I have this on my keelmark and it fits great. I feel better with my boat covered and this is a very nice cover. The price was nice especially if you have seen the price on factory covers. I would definitely buy this again and recommend to anyone with boat.</q></p>
<div class="reviewer" style="left:601px;top:1104px">Dale
  <span class="stars"><svg width="72" height="16" viewBox="0 0 72 16"><g fill="#ffd21f" stroke="#c9a000" stroke-width=".6"><use href="#st"/><use href="#st" x="18"/><use href="#st" x="36"/><use href="#st" x="54"/></g></svg></span>
</div>

<aside class="side">
  <h1 class="p-title">Centre Console With<br>Bow Rails</h1>
  <div class="p-sub">Up To 16'8" Long And 90" Wide</div>
  <div class="was">$442.00</div>
  <div class="save">You Save : <b>$110.50</b></div>
  <div class="price">$331.50</div>
  <div class="opt" style="top:175px">Color :</div>
  <div class="select" style="top:171px">--Please Select--</div>
  <div class="opt" style="top:203px">Quantity :</div>
  <div class="select" style="top:203px">1</div>

  <div class="box-head" style="top:241px">Frequently Prchased Together</div>
  <div class="box-body" style="top:283px;height:427px">
    <div class="item" style="top:13px">
      <div class="pic" role="img" aria-label="Telescoping support pole"></div>
      <div class="info"><h4>Support Pole</h4><p>works for boats<br>and trucks</p><div class="cost">$30.75 <span class="chk"></span></div></div>
    </div>
    <div class="item" style="top:98px">
      <div class="pic" role="img" aria-label="Outboard motor cover"></div>
      <div class="info"><h4>Boat Motor Cover</h4><p>heavy duty water<br>proof material</p><div class="cost">$43.06 <span class="chk"></span></div></div>
    </div>
    <div class="item" style="top:183px">
      <div class="pic" role="img" aria-label="Coiled straps and buckles"></div>
      <div class="info"><h4>132 In. Straps<br>and Buckl Pack</h4><div class="free">free!</div><div class="cost">$26.14 <span class="chk"><svg width="14" height="14" style="position:absolute;left:0;top:-4px"><path d="M2 7l3 4 8-10" fill="none" stroke="#333" stroke-width="2"/></svg></span></div></div>
    </div>
    <div class="item" style="top:269px">
      <div class="pic" role="img" aria-label="Black storage backpack"></div>
      <div class="info"><h4>Storage Bag</h4><div class="free">free!</div><div class="cost">$26.14 <span class="chk"><svg width="14" height="14" style="position:absolute;left:0;top:-4px"><path d="M2 7l3 4 8-10" fill="none" stroke="#333" stroke-width="2"/></svg></span></div></div>
    </div>
  </div>
  <div class="cart-btn">ADD TO CART</div>
  <div class="ship">Free Shipping!
    <svg width="23" height="14" viewBox="0 0 23 14"><rect x="0" y="1" width="14" height="9" fill="#2c9a3c"/><path d="M14 4h5l3 3v3h-8z" fill="#2c9a3c"/><circle cx="4" cy="11.5" r="2.2" fill="#2c9a3c" stroke="#fff"/><circle cx="18" cy="11.5" r="2.2" fill="#2c9a3c" stroke="#fff"/></svg>
  </div>

  <div class="box-head" style="top:710px">Looking For an Indoor Cover ?</div>
  <div class="box-body" style="top:752px;height:154px"></div>
  <div class="indoor-pic" role="img" aria-label="Blue indoor boat cover on a trailer"></div>
  <div class="indoor-name">Harbora 600 Denier Boat<br>Covers Fits V-Hull Runabou</div>
  <div class="indoor-price"><s>$300.00</s> <span>$138.81</span></div>
</aside>

</body>
</html>
```